Powerpoint and Word template required

We need PowerPoint and Word templates for all of our company branded materials and stationary. We have recently rebranded our website and would like something that is reflective of our new corporate branding. A sample of some of the documents we have created recently are attached and our website is below

http://corvanthealthcare.com.au/

The file 4089 Corvant_HPV_Rental_final.pdf was a document pulled together with a graphic designer recently which we think is a good starting point when thinking about the design we are after.

The word template will be used for all letters we send to clients and customers and we think we want the logo and ISO 9001 cert to only appear on the first page.

The powerpoint template has to be flexible as we use this for both marketing and training purposes. I have attached a couple of samples of the types of documents we create and note that these are very basic / crude and we would be looking for something that is a significant improvement on these

In the powerpoint template it would be good to have lots of standard layouts within the template, e.g. different 'standard layouts for multiple elements on a page including pictures and text etc.
Updates

Project Deadline Extended
Reason: Still looking for a professional yet modern template and important to us that we can see more tan just a title slide and the layout of the other slide master slides is very important to us. Many thanks, Dale

Industry/Entity Type

Healthcare

Font styles to use
Sans Serif

Colors
33a6d7

Requirements
Must have
• Templates must be versatile for use; powerpoint template must be able to be used for training materials and weel as marketing / pitch books.
• Word template must be able to be used as a basis for our corporate letter head through to RFP response type documents as well as Reference / Operating manual type of documents
• In terms of the design it must be consistent with our new corporate image which is best represented by our new website design; www.corvanthealthcare.com

```html
<!DOCTYPE html>
<html lang="en">
<head>
<meta charset="utf-8">
<title>Corvant Healthcare – Slide Master Layouts</title>
<link rel="stylesheet" href="https://fonts.googleapis.com/css2?family=Raleway:wght@300;400;600;700;800&family=Oswald:wght@300;400;500&display=swap">
<style>
  :root{
    --brand:#33a6d7;
    --brand-deep:#1f78b4;
    --brand-dark:#175f87;
    --brand-pale:#d6eef9;
    --ink:#111;
    --body:#555;
    --white:#fff;
    --frame:#000;
  }
  *{box-sizing:border-box;margin:0;padding:0}
  html,body{width:983px;height:1200px;overflow:hidden;background:var(--white)}
  body{position:relative;font-family:"Raleway",Arial,sans-serif;color:var(--ink)}

  .slide{position:absolute;width:441px;height:250px;border:2px solid var(--frame);overflow:hidden;background:var(--white)}
  .col-left{left:27px}.col-right{left:515px}
  .row-1{top:14px}.row-2{top:309px}.row-3{top:614px}.row-4{top:917px}

  .abstract-full{position:absolute;inset:0;
    background:
      linear-gradient(115deg,transparent 0 18%,rgba(255,255,255,.35) 18% 28%,transparent 28% 55%,rgba(255,255,255,.3) 55% 64%,transparent 64%),
      radial-gradient(ellipse at 45% 40%,#c9ecfb 0%,#7fcbec 40%,#3a9ccb 75%,#1d6a93 100%);}
  .abstract-floor{position:absolute;left:0;right:0;bottom:0;height:48%;
    background:
      linear-gradient(165deg,transparent 55%,rgba(31,120,180,.35) 56% 64%,transparent 65%),
      linear-gradient(to bottom,rgba(255,255,255,0) 0%,var(--brand-pale) 45%,#8fd0ec 75%,#3f9dc9 100%);}

  /* title slide */
  .cover-band{position:absolute;left:0;right:0;top:68px;height:113px;background:#f4f6f7;display:flex;align-items:center;justify-content:center;gap:14px}
  .brand-square{width:72px;height:72px;background:var(--brand-deep);border-radius:6px}
  .brand-name{font-weight:700;font-size:64px;color:var(--brand-deep);letter-spacing:-1px}

  /* title + text */
  .side-strip{position:absolute;left:0;top:0;width:106px;height:100%;background:linear-gradient(90deg,#1b6e9e,var(--brand) 55%,#1f78b4);box-shadow:3px 0 6px rgba(0,0,0,.3)}
  .title-cap{position:absolute;left:14px;top:0;width:92px;height:78px;background:linear-gradient(160deg,#fff,#e3e6e8);clip-path:polygon(0 0,100% 0,100% 62%,0 100%)}
  .title-label{position:absolute;left:25px;top:10px;font-weight:800;font-size:20px;letter-spacing:2.5px;color:var(--brand-deep)}
  .ghost-name{position:absolute;font-weight:700;color:var(--brand-deep);opacity:.18;white-space:nowrap}
  .body-list{position:absolute;left:114px;top:43px;list-style:none;font-size:9.4px;line-height:16.7px;letter-spacing:.4px;color:var(--ink)}

  /* section header */
  .section-shape{position:absolute;left:80px;top:58px}
  .section-title{position:absolute;left:0;right:0;top:96px;text-align:center;font-family:"Oswald",Arial,sans-serif;font-weight:400;font-size:23px;letter-spacing:2.5px;color:var(--white)}
  .section-sub{position:absolute;left:0;right:0;top:128px;text-align:center;font-family:"Oswald",Arial,sans-serif;font-weight:300;font-size:13px;letter-spacing:1.5px;color:#d8f0fb}

  /* headings */
  .slide-heading{position:absolute;left:26px;top:10px;font-weight:800;font-size:21px;letter-spacing:2.6px;color:var(--brand-deep)}
  .column-text{position:absolute;top:49px;width:190px;font-size:7.3px;line-height:11.5px;color:var(--ink)}
  .column-text p+p{margin-top:11.5px}
  .column-a{left:26px}.column-b{left:237px}

  /* comparison */
  .compare-band{position:absolute;left:0;right:0;top:12px;height:33px;background:var(--brand);color:var(--white);text-align:center;font-weight:700;font-size:21px;letter-spacing:2.6px;line-height:33px}
  .compare-divider{position:absolute;left:220px;top:54px;width:1.5px;height:196px;background:var(--brand)}
  .compare-list{position:absolute;top:81px;list-style:none;font-size:6px;line-height:28px;color:#333}
  .compare-a{left:24px}.compare-b{left:239px}

  /* blank */
  .blank-label{position:absolute;left:0;right:0;top:103px;text-align:center;font-weight:800;font-size:26px;letter-spacing:3px;color:var(--ink)}

  /* image + text, content */
  .image-box{position:absolute;left:55px;top:64px;width:122px;height:121px}
  .image-caption{position:absolute;left:55px;top:70px;width:122px;text-align:center;font-weight:700;font-size:11px;letter-spacing:1.5px;color:var(--ink);background:var(--white)}
  .side-text{position:absolute;left:215px;top:62px;width:185px;font-size:7.6px;line-height:12.7px;letter-spacing:.4px;color:var(--body)}
  .side-text p+p{margin-top:12.7px}
  .content-title{position:absolute;left:23px;top:88px;font-family:"Oswald",Arial,sans-serif;font-weight:500;font-size:38px;letter-spacing:3px;color:var(--brand)}
</style>
</head>
<body>

<section class="slide col-left row-1 slide-cover">
  <div class="abstract-full" role="img" aria-label="Abstract blue light-shard background"></div>
  <div class="cover-band">
    <span class="brand-square"></span>
    <span class="brand-name">Corvant</span>
  </div>
</section>

<section class="slide col-right row-1 slide-title-text">
  <div class="side-strip"></div>
  <div class="title-cap"></div>
  <span class="title-label">TITLE</span>
  <span class="ghost-name" style="left:120px;top:88px;font-size:58px">Corvant</span>
  <ul class="body-list">
    <li>Lorem ipsum dolor sit amet, consectetur adipiscing elit.</li>
    <li>Vivamus sit amet urna non massa sagittis suscipit quis sed libero.</li>
    <li>Nullam ultricies nisi at risus pretium laoreet sit amet sit amet eros.</li>
    <li>Nam feugiat nisi id tortor consectetur, a bibendum dolor pharetra.</li>
    <li>Vivamus sit amet urna non massa sagittis suscipit quis sed libero.</li>
    <li>Nullam ultricies nisi at risus pretium laoreet sit amet sit amet eros.</li>
    <li>Nam feugiat nisi id tortor consectetur, a bibendum dolor pharetra.</li>
    <li>In viverra nibh sed neque fringilla, vitae gravida diam hendrerit.</li>
    <li>Cras placerat nisi et luctus lacinia.</li>
    <li>In viverra nibh sed neque fringilla, vitae gravida diam hendrerit.</li>
    <li>Vivamus sollicitudin mi eget dui dignissim dignissim.</li>
    <li>Fusce dignissim massa a odio eleifend placerat.</li>
  </ul>
</section>

<section class="slide col-left row-2 slide-section">
  <svg class="section-shape" width="288" height="131" viewBox="0 0 288 131" aria-hidden="true">
    <defs>
      <linearGradient id="panel" x1="0" x2="0" y1="0" y2="1"><stop offset="0" stop-color="#f3f4f5"/><stop offset="1" stop-color="#e4e6e8"/></linearGradient>
    </defs>
    <polygon points="0,0 288,0 262,131 26,131" fill="#d9dcde"/>
    <polygon points="12,0 276,0 252,131 36,131" fill="url(#panel)"/>
    <polygon points="6,26 282,26 266,106 22,106" fill="#1f78b4"/>
    <polygon points="18,26 270,26 256,106 32,106" fill="#33a6d7"/>
  </svg>
  <div class="section-title">SECTION HEADER</div>
  <div class="section-sub">SUB TEXT</div>
</section>

<section class="slide col-right row-2 slide-two-contents">
  <div class="abstract-floor" role="img" aria-label="Soft blue abstract light streaks"></div>
  <h2 class="slide-heading">TWO CONTENTS</h2>
  <div class="column-text column-a">
    <p>Lorem ipsum dolor sit amet, consectetuer adipiscing elit. Donec odio. Quisque volutpat mattis eros. Nullam malesuada erat ut turpis. Suspendisse urna nibh, viverra non, semper suscipit, posuere a, pede.</p>
    <p>Donec nec justo eget felis facilisis fermentum. Aliquam porttitor mauris sit amet orci. Aenean dignissim pellentesque felis.</p>
    <p>Morbi in sem quis dui placerat ornare. Pellentesque odio nisi, euismod in, pharetra a, ultricies in, diam. Sed arcu. Cras consequat.</p>
  </div>
  <div class="column-text column-b">
    <p>Lorem ipsum dolor sit amet, consectetuer adipiscing elit. Donec odio. Quisque volutpat mattis eros. Nullam malesuada erat ut turpis. Suspendisse urna nibh, viverra non, semper suscipit, posuere a, pede.</p>
    <p>Donec nec justo eget felis facilisis fermentum. Aliquam porttitor mauris sit amet orci. Aenean dignissim pellentesque felis.</p>
    <p>Morbi in sem quis dui placerat ornare. Pellentesque odio nisi, euismod in, pharetra a, ultricies in, diam. Sed arcu. Cras consequat.</p>
  </div>
</section>

<section class="slide col-left row-3 slide-comparison">
  <div class="abstract-floor" role="img" aria-label="Soft blue abstract light streaks" style="height:58%"></div>
  <div class="compare-band">COMPARISON</div>
  <div class="compare-divider"></div>
  <ol class="compare-list compare-a">
    <li>1. Lorem ipsum dolor sit amet, consectetuer adipiscing elit.</li>
    <li>2. Aliquam tincidunt mauris eu risus.</li>
    <li>3. Vestibulum auctor dapibus neque.</li>
    <li>4. Nunc dignissim risus id metus.</li>
    <li>5. Cras ornare tristique elit.</li>
  </ol>
  <ol class="compare-list compare-b">
    <li>1. Lorem ipsum dolor sit amet, consectetuer adipiscing elit.</li>
    <li>2. Aliquam tincidunt mauris eu risus.</li>
    <li>3. Vestibulum auctor dapibus neque.</li>
    <li>4. Nunc dignissim risus id metus.</li>
    <li>5. Cras ornare tristique elit.</li>
  </ol>
</section>

<section class="slide col-right row-3 slide-blank">
  <div class="abstract-full" role="img" aria-label="Abstract blue light-shard background"></div>
  <span class="ghost-name" style="left:60px;top:70px;font-size:70px;opacity:.25">Corvant</span>
  <div class="blank-label">BLANK</div>
</section>

<section class="slide col-left row-4 slide-image-text">
  <div class="abstract-floor" role="img" aria-label="Soft blue abstract light streaks"></div>
  <svg class="image-box" viewBox="0 0 122 121" aria-hidden="true">
    <rect x=".5" y=".5" width="121" height="120" fill="#fff" stroke="#111"/>
    <line x1="0" y1="0" x2="122" y2="121" stroke="#111"/>
    <line x1="122" y1="0" x2="0" y2="121" stroke="#111"/>
  </svg>
  <div class="image-caption">IMAGE</div>
  <div class="side-text">
    <p>Lorem ipsum dolor sit amet, consectetuer adipiscing elit. Donec odio. Quisque volutpat mattis eros. Nullam malesuada erat ut turpis. Suspendisse urna nibh, viverra non, semper suscipit, posuere a, pede.</p>
    <p>Donec nec justo eget felis facilisis fermentum. Aliquam porttitor mauris sit amet orci. Aenean dignissim pellentesque felis.</p>
  </div>
</section>

<section class="slide col-right row-4 slide-content">
  <div class="abstract-floor" role="img" aria-label="Soft blue abstract light streaks"></div>
  <div class="content-title">CONTENT</div>
  <div class="side-text">
    <p>Lorem ipsum dolor sit amet, consectetuer adipiscing elit. Donec odio. Quisque volutpat mattis eros. Nullam malesuada erat ut turpis. Suspendisse urna nibh, viverra non, semper suscipit, posuere a, pede.</p>
    <p>Donec nec justo eget felis facilisis fermentum. Aliquam porttitor mauris sit amet orci. Aenean dignissim pellentesque felis.</p>
  </div>
</section>

</body>
</html>
```